Crafted Ember Website

Would like a website designed for my fitness and nutrition coaching company Craft Ember. I have a company logo and would like to keep the page layout clean and simple. Needs to look great on computer and mobile devices.

Target Market(s)

Target market is individuals looking to make changes in their health and nutrition with the help of an online coach.

Industry/Entity Type

Fitness

Number of Pages Required

2 page

Colors
3176b5
0355a3
85acd3
cedeed
f8fcfd
ffffff

Requirements
Must have
• The first page should have the company logo and name towards the top and below that client before and after photos scrolling or displaying in some manner. Also would like a section that states services offered and a section about myself since I am the primary coach for clients.

```html
<!DOCTYPE html>
<html lang="en">
<head>
<meta charset="utf-8">
<title>Crafted Ember – Fitness &amp; Nutrition Coaching</title>
<link href="https://fonts.googleapis.com/css2?family=Roboto:wght@400;500;700&family=Open+Sans:wght@400;600&display=swap" rel="stylesheet">
<style>
:root{
  --blue:#1a6fbf;
  --blue-dark:#0355a3;
  --blue-mid:#3176b5;
  --blue-soft:#85acd3;
  --blue-pale:#cedeed;
  --ice:#f8fcfd;
  --white:#ffffff;
  --ink:#222222;
  --grey:#666666;
  --footer:#1d1d1d;
  --footer-line:#3a3a3a;
}
*{box-sizing:border-box;margin:0;padding:0}
html,body{width:1200px;height:3237px;overflow:hidden}
body{font-family:"Open Sans",Arial,sans-serif;color:var(--ink);background:var(--white);position:relative}
h1,h2,h3,h4,.nav,.btn{font-family:"Roboto",Arial,sans-serif}
section,header,footer{position:absolute;left:0;width:1200px;overflow:hidden}
.btn{display:inline-block;background:var(--blue);color:var(--white);font-size:15px;font-weight:500;border-radius:5px;text-align:center;text-transform:uppercase}

/* hero */
.hero{top:0;height:582px}
.hero-photo{position:absolute;inset:0;background:linear-gradient(110deg,#7a5a3e 0%,#b58a5e 30%,#d9b48a 55%,#8a6a4e 80%,#4e3c2e 100%)}
.hero-shade{position:absolute;inset:0;background:rgba(20,25,35,.25)}
.topbar{position:absolute;right:0;top:0;width:520px;height:40px;background:var(--blue);color:var(--white);font-size:13px;display:flex;align-items:center;gap:40px;padding-left:80px;clip-path:polygon(28px 0,100% 0,100% 100%,0 100%)}
.topbar span{display:flex;align-items:center;gap:10px}
.topbar i{width:22px;height:22px;border-radius:50%;background:var(--white);display:inline-block}
.brand-box{position:absolute;left:0;top:0;width:350px;height:124px;background:var(--white);clip-path:polygon(0 0,100% 0,82% 100%,0 100%);display:flex;flex-direction:column;align-items:flex-start;justify-content:center;padding-left:98px}
.brand{display:flex;align-items:center;gap:10px;font-family:"Roboto",Arial,sans-serif;font-weight:700;font-size:19px;color:var(--blue-dark);letter-spacing:.5px}
.brand i{width:26px;height:26px;background:var(--blue);display:inline-block}
.nav{position:absolute;top:66px;left:468px;display:flex;gap:32px;font-size:15px;font-weight:500;color:var(--white)}
.nav .active{color:var(--blue)}
.hero-copy{position:absolute;top:208px;left:0;width:1200px;text-align:center;color:var(--white)}
.hero-copy h1{font-size:46px;font-weight:700;letter-spacing:1px}
.hero-copy p{font-family:"Roboto",Arial,sans-serif;font-size:27px;font-weight:500;line-height:42px;margin-top:12px}
.hero-copy .btn{margin-top:36px;width:156px;height:44px;line-height:44px}
.dots{position:absolute;top:533px;left:576px;display:flex;gap:4px}
.dots i{width:12px;height:12px;border-radius:50%;border:2px solid var(--white)}
.dots i.on{background:var(--white)}
.corner{position:absolute;right:0;bottom:0}

/* about */
.about{top:582px;height:515px;background:var(--white)}
.about-copy{position:absolute;left:98px;top:76px;width:455px}
.about h2{font-size:32px;font-weight:700;color:#333}
.about h3{font-size:20px;font-weight:500;margin-top:14px;color:#222}
.about p{font-size:13px;line-height:20px;color:var(--grey);margin-top:10px}
.about .btn{margin-top:22px;width:140px;height:44px;line-height:44px}
.about-photo-wrap{position:absolute;left:598px;top:76px;width:500px;height:336px;border:1px solid #ddd;padding:6px;background:var(--white)}
.about-photo{width:100%;height:100%;background:linear-gradient(130deg,#8d8f94,#c6c7cb 45%,#555a62)}
.about-diamond{position:absolute;left:612px;top:24px}

/* mission band */
.mission{top:1097px;height:353px;background:linear-gradient(90deg,#1f68ae,#2a78bf 50%,#1c64aa)}
.mission-copy{position:absolute;top:82px;left:0;width:1200px;text-align:center;color:var(--white)}
.mission h2{font-size:29px;font-weight:500}
.mission p{font-size:16px;line-height:26px;width:730px;margin:20px auto 0;font-weight:600}
.mission .ghost{display:inline-block;margin-top:28px;width:154px;height:48px;line-height:46px;border:1.5px solid var(--white);border-radius:5px;font-family:"Roboto",Arial,sans-serif;font-size:15px;font-weight:500}

/* services */
.services{top:1450px;height:515px;background:var(--white)}
.services h2{position:absolute;top:72px;width:1200px;text-align:center;font-size:29px;font-weight:500;color:#222}
.service{position:absolute;top:148px;width:210px;text-align:center}
.service svg{display:block;margin:0 auto}
.service h4{font-size:17px;font-weight:500;margin-top:12px}
.service p{font-size:12.5px;line-height:20px;color:var(--grey);margin-top:10px}
.services .btn{position:absolute;left:537px;top:400px;width:130px;height:46px;line-height:46px}

/* gallery */
.gallery{top:1965px;height:520px}
.gallery-bg{position:absolute;inset:0;background:linear-gradient(180deg,#6d6e73,#7d7e82 50%,#66676c)}
.gallery h2{position:absolute;top:74px;width:1200px;text-align:center;font-size:29px;font-weight:500;color:var(--white)}
.card{position:absolute;top:140px;width:310px;height:325px;border:1px solid rgba(255,255,255,.6)}
.card-photo{height:240px;background:linear-gradient(180deg,#f4f4f4,#e6e6e6);display:flex;gap:4px;padding:0}
.card-photo div{flex:1;background:linear-gradient(180deg,#f1ece8,#cfc6c0 60%,#e9e9ea)}
.card-info{height:83px;background:rgba(90,90,95,.85);color:var(--white);text-align:center;padding-top:12px}
.card-info h4{font-size:17px;font-weight:500}
.card-info p{font-size:13px;margin-top:10px}
.card-info b{font-weight:600}
.arrow{position:absolute;top:272px}

/* subscribe */
.subscribe{top:2485px;height:380px}
.subscribe-bg{position:absolute;inset:0;background:linear-gradient(90deg,#eef2f6,#dfe6ee 60%,#cfd9e4)}
.subscribe h2{position:absolute;left:100px;top:170px;font-size:29px;line-height:44px;font-weight:500;color:#222}
.field{position:absolute;left:604px;width:480px;height:42px;border:1px solid #bbb;background:rgba(255,255,255,.35);font-size:12px;color:#666;padding:12px 18px}
.subscribe .btn{position:absolute;left:956px;top:264px;width:128px;height:44px;line-height:44px}

/* footer */
.site-footer{top:2865px;height:372px;background:var(--footer);color:#ddd}
.site-footer .brand{position:absolute;left:98px;top:150px;color:var(--blue-mid);font-size:22px}
.site-footer .brand i{width:30px;height:30px}
.fcol{position:absolute;top:56px}
.fcol h4{font-size:16px;font-weight:500;color:var(--white);letter-spacing:.5px}
.fcol ul{list-style:none;margin-top:22px}
.fcol li{font-size:12.5px;line-height:23px;color:#ddd;display:flex;gap:8px;align-items:flex-start}
.fcol li svg{margin-top:6px;flex:none}
.fline{position:absolute;left:98px;top:277px;width:1002px;height:1px;background:var(--footer-line)}
.copy{position:absolute;left:98px;top:307px;font-size:12px;color:#ccc}
.socials{position:absolute;left:1000px;top:307px;display:flex;gap:8px}
.socials i{width:12px;height:12px;border-radius:50%;background:#ccc;display:block}
</style>
</head>
<body>

<header class="hero">
  <div class="hero-photo" role="img" aria-label="Athlete training on a treadmill in a sunlit gym"></div>
  <div class="hero-shade"></div>
  <div class="topbar">
    <span><i></i>info@craftedember.com</span>
    <span><i></i>+1 555 014 2290</span>
  </div>
  <div class="brand-box">
    <div class="brand"><i></i>CRAFTED EMBER</div>
  </div>
  <nav class="nav">
    <span class="active">Home</span><span>About Us</span><span>WOD</span><span>Features</span><span>Success Stories</span><span>Contact Us</span>
    <svg width="16" height="16" viewBox="0 0 16 16"><circle cx="6.5" cy="6.5" r="5" fill="none" stroke="#fff" stroke-width="2"/><line x1="10" y1="10" x2="15" y2="15" stroke="#fff" stroke-width="2"/></svg>
  </nav>
  <div class="hero-copy">
    <h1>CRAFTED EMBER</h1>
    <p>It Is A Long Established Fact That A Reader Will<br>Be Distracted By Readable Of A Page.</p>
    <span class="btn">Join Now !</span>
  </div>
  <div class="dots"><i class="on"></i><i></i><i></i></div>
  <svg class="corner" width="120" height="100" viewBox="0 0 120 100"><polygon points="120,0 120,100 0,100" fill="#1a6fbf"/><polygon points="110,0 120,0 10,100 0,100" fill="#fff"/></svg>
</header>

<section class="about">
  <div class="about-copy">
    <h2>About Myself</h2>
    <h3>I Am The Primary Coach For Clients</h3>
    <p>Sed ut perspiciatis unde omnis iste natus error sit voluptatem accusantium doloremque laudantium, totam rem aperiam, eaque ipsa quae ab illo inventore veritatis et quasi architecto beatae vitae dicta sunt explicabo.</p>
    <p>Nemo enim ipsam voluptatem quia voluptas sit aspernatur aut odit aut fugit, sed quia consequuntur magni dolores eos qui ratione voluptatem sequi nesciunt.</p>
    <span class="btn">Read More</span>
  </div>
  <svg class="about-diamond" width="470" height="440" viewBox="0 0 470 440"><polygon points="235,2 468,220 235,438 2,220" fill="none" stroke="#3176b5" stroke-width="2"/></svg>
  <div class="about-photo-wrap"><div class="about-photo" role="img" aria-label="Coach guiding a client through a sit-up in the gym"></div></div>
</section>

<section class="mission">
  <div class="mission-copy">
    <h2>We Are #1 Fitness And Nutrition Coaching Company</h2>
    <p>Sed ut perspiciatis unde omnis iste natus error sit voluptatem accusantium doloremque laudantium, totam rem aperiam, eaque ipsa quae ab illo inventore veritatis et quasi architecto beatae vitae dicta sunt explicabo.</p>
    <span class="ghost">Get Started</span>
  </div>
  <svg class="corner" width="180" height="130" viewBox="0 0 180 130"><polygon points="180,0 180,130 0,130" fill="#fff"/><polygon points="180,20 180,130 60,130" fill="#6b6c70"/></svg>
</section>

<section class="services">
  <h2>Services Offered</h2>
  <div class="service" style="left:87px">
    <svg width="110" height="110" viewBox="0 0 110 110"><polygon points="55,2 108,55 55,108 2,55" fill="none" stroke="#333" stroke-width="2"/><circle cx="44" cy="66" r="10" fill="none" stroke="#1a6fbf" stroke-width="3"/><path d="M44 66 L60 42 L68 42 M56 48 L66 66" fill="none" stroke="#1a6fbf" stroke-width="3"/></svg>
    <h4>WOD</h4>
    <p>Sed ut piciatis unde omni natus error sit voluptatem accusa doloremque laudantium..</p>
  </div>
  <div class="service" style="left:357px">
    <svg width="110" height="110" viewBox="0 0 110 110"><polygon points="55,2 108,55 55,108 2,55" fill="none" stroke="#333" stroke-width="2"/><circle cx="55" cy="58" r="15" fill="none" stroke="#1a6fbf" stroke-width="3"/><path d="M55 58 L55 48 M51 38 L59 38 M55 38 L55 43" stroke="#1a6fbf" stroke-width="3"/></svg>
    <h4>Express WOD</h4>
    <p>Sed ut piciatis unde omni natus error sit voluptatem accusa doloremque laudantium..</p>
  </div>
  <div class="service" style="left:625px">
    <svg width="110" height="110" viewBox="0 0 110 110"><polygon points="55,2 108,55 55,108 2,55" fill="none" stroke="#333" stroke-width="2"/><path d="M42 40 L42 72 M68 40 L68 72 M42 56 L68 56" stroke="#1a6fbf" stroke-width="4"/></svg>
    <h4>Fundamentals</h4>
    <p>Sed ut piciatis unde omni natus error sit voluptatem accusa doloremque laudantium..</p>
  </div>
  <div class="service" style="left:893px">
    <svg width="110" height="110" viewBox="0 0 110 110"><polygon points="55,2 108,55 55,108 2,55" fill="none" stroke="#333" stroke-width="2"/><path d="M36 46 L74 46 M55 46 L55 68 M40 70 L70 70" stroke="#1a6fbf" stroke-width="4"/></svg>
    <h4>Endurance</h4>
    <p>Sed ut piciatis unde omni natus error sit voluptatem accusa doloremque laudantium..</p>
  </div>
  <span class="btn">View All</span>
</section>

<section class="gallery">
  <div class="gallery-bg" role="img" aria-label="Dimmed gym interior behind the gallery"></div>
  <h2>Photo Gallery</h2>
  <svg class="arrow" style="left:28px" width="20" height="30" viewBox="0 0 20 30"><path d="M16 3 L4 15 L16 27" fill="none" stroke="#fff" stroke-width="3"/></svg>
  <div class="card" style="left:100px">
    <div class="card-photo" role="img" aria-label="Client before and after photos"><div></div><div></div></div>
    <div class="card-info"><h4>Mara Velloso</h4><p><b>Package :</b> WOD &nbsp;&nbsp;|&nbsp;&nbsp; 100 Days</p></div>
  </div>
  <div class="card" style="left:445px">
    <div class="card-photo" role="img" aria-label="Client before and after photos"><div></div><div></div></div>
    <div class="card-info"><h4>Ines Hartwell</h4><p><b>Package :</b> Express WOD &nbsp;&nbsp;|&nbsp;&nbsp; 30 Days</p></div>
  </div>
  <div class="card" style="left:790px">
    <div class="card-photo" role="img" aria-label="Client before and after photos"><div></div><div></div></div>
    <div class="card-info"><h4>Dana Kirova</h4><p><b>Package :</b> WOD &nbsp;&nbsp;|&nbsp;&nbsp; 190 Days</p></div>
  </div>
  <svg class="arrow" style="left:1150px" width="20" height="30" viewBox="0 0 20 30"><path d="M4 3 L16 15 L4 27" fill="none" stroke="#fff" stroke-width="3"/></svg>
  <svg class="corner" width="180" height="140" viewBox="0 0 180 140"><polygon points="180,0 180,140 0,140" fill="#fff"/><polygon points="180,0 180,20 20,140 0,140" fill="#1a6fbf"/></svg>
</section>

<section class="subscribe">
  <div class="subscribe-bg" role="img" aria-label="Faded group workout class"></div>
  <h2>Subscribe Us For Special Offers<br>And Health Tips</h2>
  <div class="field" style="top:142px">Name</div>
  <div class="field" style="top:202px">Email</div>
  <span class="btn">Submit</span>
</section>

<footer class="site-footer">
  <div class="brand"><i></i>CRAFTED EMBER</div>
  <div class="fcol" style="left:462px">
    <h4>LINKS</h4>
    <ul><li>Home</li><li>About Us</li><li>WOD</li><li>Features</li><li>Success Stories</li><li>Contact Us</li></ul>
  </div>
  <div class="fcol" style="left:678px">
    <h4>EXTRAS</h4>
    <ul><li>Lorem ipsum</li><li>Dolor sit amet</li><li>Consectetur adipiscing elit</li><li>Cras rutrum</li><li>Massa pellentesque</li></ul>
  </div>
  <div class="fcol" style="left:920px">
    <h4>CONTACT US</h4>
    <ul>
      <li><svg width="11" height="11" viewBox="0 0 11 11"><path d="M2 1 L4 1 L5 3.5 L3.8 4.5 Q5 7 6.5 7.2 L7.5 6 L10 7 L10 9 Q5 10.5 1 2 Z" fill="#ddd"/></svg>+1 555 014 2290</li>
      <li><svg width="11" height="9" viewBox="0 0 11 9"><rect x="0" y="0" width="11" height="9" fill="#ddd"/><path d="M0 0 L5.5 5 L11 0" fill="none" stroke="#1d1d1d"/></svg>info@craftedember.com</li>
      <li><svg width="9" height="12" viewBox="0 0 9 12"><path d="M4.5 12 L1 6 A4 4 0 1 1 8 6 Z" fill="#ddd"/><circle cx="4.5" cy="4.2" r="1.5" fill="#1d1d1d"/></svg>Lorem Ipsum, dolor sirt<br>Coporate, 000001</li>
    </ul>
  </div>
  <div class="fline"></div>
  <p class="copy">Copy Rights © 2017, Crafted Ember. All Rights Reserved.</p>
  <div class="socials"><i></i><i></i><i></i><i></i><i></i></div>
</footer>

</body>
</html>
```